Non-Profit Needs Web Redesign for Revolutionary Grieving Process

We need a redesign of our website that represents the expansive social goal of changing the worldview of how our culture understands and can heal from the universal experience of grief. The Quiet Harbor process is a revolutionary method that allows an individual to resolve the underlying issue that cause the painful experience of loss.The color scheme should be in the green family that is soft and light yet professional and connotes change and growth. The final design should communicate simplistically with white space and strong typography a global viewpoint of change in a fundamental human experience. The redesign should represent the non-profit organization's perspective of openness and possibility without being flashy or corporate. see www.mendlight.org
Grief professional, hospitals, hospices
Non Profit
Coded - Design and coding required
1 page

```html
<!DOCTYPE html>
<html lang="en">
<head>
<meta charset="utf-8">
<title>MendLight.org – A New Path Through Loss</title>
<link rel="stylesheet" href="https://fonts.googleapis.com/css2?family=Raleway:wght@400;500&family=Open+Sans:wght@400;600&display=swap">
<style>
:root{
  --green:#6aaa1e;
  --green-light:#8ccf3a;
  --green-dark:#4f8a12;
  --orange:#ff9c00;
  --orange-light:#ffb52e;
  --text:#444;
  --muted:#666;
  --rule:#d9d9d9;
  --white:#fff;
  --footer-top:#f7f7f7;
  --footer-bottom:#e6e6e6;
}
*{margin:0;padding:0;box-sizing:border-box}
html,body{width:1101px;height:1200px;overflow:hidden;background:var(--white)}
body{position:relative;font-family:"Open Sans",sans-serif;color:var(--text)}
.abs{position:absolute}

.brand{left:159px;top:26px}
.brand-name{font-family:"Raleway",sans-serif;font-weight:500;font-size:27px;color:var(--green);line-height:1}
.brand-tagline{font-family:"Open Sans",sans-serif;font-size:10px;color:#333;margin-top:9px;margin-left:1px}

.main-nav{left:0;top:94px;width:1101px;height:42px;background:linear-gradient(#8fd13c,#6cb423)}
.main-nav ul{list-style:none;display:flex;padding-left:164px;height:100%;align-items:center}
.main-nav li{font-family:"Raleway",sans-serif;font-weight:500;font-size:12.5px;color:var(--white);margin-right:29px}

.hero{left:0;top:136px;width:1101px;height:401px}
.hero-photo{position:absolute;inset:0;background:linear-gradient(100deg,#4d7a33 0%,#6f9a45 35%,#9fb884 58%,#d9d6cb 75%,#c7d3e0 100%)}
.hero-copy{position:absolute;left:158px;top:116px;color:var(--white)}
.hero-kicker{font-family:"Raleway",sans-serif;font-size:24px;font-weight:400}
.hero-title{font-family:"Raleway",sans-serif;font-size:36px;font-weight:500;margin-top:4px}
.hero-text{font-size:10.5px;line-height:17px;width:380px;margin-top:6px}
.hero-dots{display:flex;gap:4px;margin-top:12px}
.hero-dots span{width:14px;height:14px;border-radius:50%;background:var(--white)}
.hero-dots span.active{background:var(--orange)}

.feature{top:585px;width:250px;text-align:center}
.feature svg{display:block;margin:0 auto;height:52px}
.feature h2{font-family:"Raleway",sans-serif;font-weight:400;font-size:16.5px;color:#333;margin-top:21px;white-space:nowrap}
.feature h2 em{font-style:normal;color:var(--green)}
.feature p{font-size:9px;line-height:17.5px;color:var(--muted);margin-top:5px;padding:0 8px}
.btn{display:inline-block;height:27px;line-height:27px;padding:0 17px;font-size:10.5px;color:var(--white);border-radius:2px;text-transform:uppercase}
.btn-green{background:linear-gradient(#7cbc2a,#4f8a12);margin-top:12px}
.btn-orange{background:linear-gradient(#ffb52e,#ff9c00)}

.divider{left:160px;top:821px;width:781px;height:1px;background:var(--rule)}

.about{left:162px;top:870px;width:490px}
.about h2{font-family:"Raleway",sans-serif;font-weight:400;font-size:22.5px;color:#333}
.about .lead{font-size:10.5px;line-height:18px;color:var(--muted);margin-top:10px}
.about .body{font-size:9px;line-height:17.5px;color:var(--muted);margin-top:4px}
.about .btn{margin-top:13px}

.testimonial{left:691px;top:866px;width:250px;height:186px;background:var(--orange);border-top:5px solid var(--orange-light);text-align:center;color:var(--white);padding:22px 18px 0}
.testimonial h2{font-family:"Raleway",sans-serif;font-weight:400;font-size:21px}
.testimonial p{font-size:8.5px;line-height:16px;margin-top:7px}
.testimonial cite{display:block;font-style:normal;font-size:11.5px;margin-top:4px}

.site-footer{left:0;top:1104px;width:1101px;height:96px;border-top:1px solid var(--rule);background:linear-gradient(var(--footer-top),var(--footer-bottom))}
.footer-nav{position:absolute;left:169px;top:31px;font-family:"Raleway",sans-serif;font-weight:500;font-size:11px;color:#222;letter-spacing:.2px}
.footer-nav span{margin:0 5px}
.copyright{position:absolute;left:169px;top:54px;font-size:8.5px;color:#333}
.social{position:absolute;left:866px;top:30px;display:flex;gap:8px}
.social span{width:13px;height:13px;border-radius:50%;background:#5d7f9e}
</style>
</head>
<body>

<header class="abs brand">
  <div class="brand-name">MendLight.org</div>
  <div class="brand-tagline">A New Path Through Loss</div>
</header>

<nav class="abs main-nav">
  <ul>
    <li>Home</li>
    <li>About Us</li>
    <li>Our ProcessTestimonials</li>
    <li>How to Get Grief Support</li>
    <li>Professional Training</li>
    <li>Blog</li>
    <li>Contact</li>
  </ul>
</nav>

<section class="abs hero">
  <div class="hero-photo" role="img" aria-label="Photo of an elderly woman and a caregiver talking in a sunny park"></div>
  <div class="hero-copy">
    <div class="hero-kicker">Donec dictum lectus non</div>
    <div class="hero-title">Pellentesque faucibus</div>
    <p class="hero-text">Curabitur iaculis tempus eros Curabitur vel mi sit amet magna malesuada ultrices Ut nisi erat fermentum vel congue id euismod in elit</p>
    <div class="hero-dots"><span class="active"></span><span></span><span></span><span></span></div>
  </div>
</section>

<article class="abs feature" style="left:145px">
  <svg viewBox="0 0 40 52" aria-hidden="true"><path d="M20 2C14 16 4 26 4 36a16 16 0 0 0 32 0C36 26 26 16 20 2z" fill="var(--green)"/><path d="M20 32c-2 4-3 6-3 8a3 3 0 0 0 6 0c0-2-1-4-3-8z" fill="#fff"/></svg>
  <h2>What is Quiet Harbor<em>?</em></h2>
  <p>Curabitur iaculis tempus eros Curabitur vel mi sit amet magna malesuada ultrices Ut nisi erat fermentum vel congue id euismod in elit Fusce ultricies rci ac feugiat suscipit leo massa sodales velit</p>
  <span class="btn btn-green">Read More</span>
</article>

<article class="abs feature" style="left:432px">
  <svg viewBox="0 0 40 52" aria-hidden="true"><path d="M8 46C16 40 22 30 24 10" stroke="var(--green)" stroke-width="3" fill="none" stroke-linecap="round"/><ellipse cx="26" cy="8" rx="4" ry="7" fill="var(--green)"/><ellipse cx="32" cy="20" rx="7" ry="4" fill="var(--green)" transform="rotate(-20 32 20)"/><ellipse cx="13" cy="22" rx="7" ry="4" fill="var(--green)" transform="rotate(30 13 22)"/><ellipse cx="30" cy="34" rx="7" ry="4" fill="var(--green)" transform="rotate(-10 30 34)"/><ellipse cx="8" cy="36" rx="6" ry="3.5" fill="var(--green)" transform="rotate(20 8 36)"/></svg>
  <h2>The Quiet Harbor Process</h2>
  <p>Curabitur iaculis tempus eros Curabitur vel mi sit amet magna malesuada ultrices Ut nisi erat fermentum vel congue id euismod in elit Fusce ultricies orci ac feugiat suscipit leo massa sodales velit</p>
  <span class="btn btn-green">Read More</span>
</article>

<article class="abs feature" style="left:711px">
  <svg viewBox="0 0 52 52" aria-hidden="true"><circle cx="26" cy="26" r="24" fill="var(--green)"/><text x="26" y="38" text-anchor="middle" font-family="Open Sans,sans-serif" font-weight="700" font-size="34" fill="#fff">?</text></svg>
  <h2>Understanding Quiet Harbor</h2>
  <p>Curabitur iaculis tempus eros Curabitur vel mi sit amet magna malesuada ultrices Ut nisi erat fermentum vel congue id euismod in elit Fusce ultricies orci ac feugiat suscipit leo massa sodales</p>
  <span class="btn btn-green">Read More</span>
</article>

<div class="abs divider"></div>

<section class="abs about">
  <h2>About MendLight Org</h2>
  <p class="lead">Curabitur iaculis tempus eros Curabitur vel mi sit amet magna malesuada ultrices Ut nisi erat fermentum vel congue id euismod in elit Fusce ultricies orci ac feugiat suscipit</p>
  <p class="body">Morbi ornare gravida elit Integer congue augue et malesuada iaculis ipsum dui aliquet felis at cursus magna nisl nec elit Praesent elementum elit at tellus nec ultricies sit amet porttitor mattis enim In massa libero interdum nec interdum vel blandit sed nulla In ullamcorper est eget tempor cursus neque mi consectetuer mi</p>
  <span class="btn btn-orange">Read More</span>
</section>

<aside class="abs testimonial">
  <h2>Testimonial</h2>
  <p>truly revolutionary.... Martin has an uncanny ability to articulate deep transformation processes into straightforward worksheets. I have worked with most of Martin's processes and can attest to their amazing delivery of inner awareness.</p>
  <cite>By Author Name</cite>
</aside>

<footer class="abs site-footer">
  <div class="footer-nav">HOME<span>|</span>ABOUT US<span>|</span>SERVICES<span>|</span>OUR PROCESS<span>|</span>TRAINING<span>|</span>BLOG<span>|</span>CONTACT</div>
  <div class="copyright">© 2015 Company Name &nbsp;All right reserved &nbsp;Term of Use</div>
  <div class="social" aria-label="Social links"><span></span><span></span><span></span><span></span></div>
</footer>

</body>
</html>
```